依頼概要
■依頼の目的/概要
弊社が販売しているゆず酒月夜のささやきプレミアムの東京限定ラベルデザインをお願いします。

■依頼詳細
今回は月夜のささやきプレミアムというネームをはずして雪見桃ノ詩という商品を東京限定販売予定です。海外の旅行客のお土産やレトロデザインで目を惹ける飲食店様で扱ってもらえる位置づけを考えておりますので宜しくお願いします。
ラベルデザイン:65㎜×55㎜ 縦長楕円
ボトル容量:425㎖のオリジナル瓶を使用
ブランド名:月夜のささやき
商品名:雪見桃ノ詩(クラフタルコンペで決定したネームです)
■その他要望
1900年初頭のパリ アールヌーヴォーデザインが舶来品として東京に入ってきたものに皆が憧れた
大正~昭和初期に銀座で和リキュールが若者の間でブームになった
その復刻版的な感じのレトロデザインでボトル形状とマッチングさせていただきたい
必須事項:商品名明記 縦横可 レトロフォント金文体がイメージに近いが自由にデザインしてください
女性をモデルにでざいんを取り入れて下さい
ブランド名はデザインイメージから外して下さい。
その他何かご不明な点がございましたら、お気軽にご質問下さい。
よろしくお願いいたします。
応募ありがとうございます
弊社としては大正・昭和当時のレトロ感の打ち出しが重要と考えておりますので
宜しくお願いします。
■ 選んだ理由

弊社内においてアンケート投票の結果をもとに決定させていただきました。今回は特に女性の意見を参考にさせていただきました。購入ターゲットとしては比率は女性のほうが多い商品にとの思いをこめておりますので柔らかい印象の作品を当選させていただきました。本当にたくさんの応募ありがとうございました。

■ 提案者全員のお礼・コメント

たくさんの提案ありがとうございました。今回はゆず酒のラベルにはお一人の当選しかできませんでしたが、弊社他の果実リキュールのラベルデザイン変更も考えておりますのでその際にはまた応募の程、宜しくお願い致します。

```html
<!DOCTYPE html>
<html lang="ja">
<head>
<meta charset="utf-8">
<title>雪見桃ノ詩 ラベル</title>
<link rel="stylesheet" href="https://fonts.googleapis.com/css2?family=Zen+Antique&family=Shippori+Mincho+B1:wght@600&family=Great+Vibes&display=swap">
<style>
  :root{
    --paper:#f6f3ea;
    --navy:#14233a;
    --navy-deep:#0c1626;
    --gold:#d9b25a;
    --gold-light:#f0d690;
    --leaf:#2f4a3a;
    --yuzu:#e9c74a;
    --kimono:#9b2f2a;
    --skin-tone:#e8d3bd;
  }
  html,body{margin:0;padding:0;overflow:hidden;}
  body{width:849px;height:1200px;background:var(--paper);position:relative;}
  .neck-label{
    position:absolute;left:214px;top:70px;width:420px;height:170px;
    background:var(--navy);box-sizing:border-box;
    border:4px solid var(--gold);box-shadow:inset 0 0 0 6px var(--navy),inset 0 0 0 8px var(--gold);
  }
  .neck-label .brand-small{
    position:absolute;left:0;right:0;top:36px;text-align:center;
    font-family:"Zen Antique",serif;color:var(--gold-light);font-size:44px;letter-spacing:6px;
  }
  .neck-label .fruit-mark{
    position:absolute;left:50%;top:104px;width:36px;height:36px;margin-left:-18px;
    border-radius:50%;background:radial-gradient(circle at 40% 35%,#f6e08a,var(--yuzu));
  }
  .oval-label{
    position:absolute;left:124px;top:330px;width:600px;height:780px;
    border-radius:50%;overflow:hidden;box-sizing:border-box;
    background:radial-gradient(ellipse at 50% 45%,var(--navy),var(--navy-deep));
    border:12px solid var(--gold);
    box-shadow:inset 0 0 0 6px var(--navy-deep),inset 0 0 0 9px var(--gold);
  }
  .art{position:absolute;}
  .art-foliage{
    left:-40px;top:-40px;width:680px;height:260px;border-radius:50%;
    background:radial-gradient(ellipse at 50% 30%,#5f7a3c 0%,var(--leaf) 45%,rgba(20,35,58,0) 75%);
  }
  .art-lamp{
    left:70px;top:150px;width:60px;height:110px;border-radius:12px;
    background:linear-gradient(#e9d58a,#b98d3e);opacity:.85;
  }
  .art-yuzu{
    left:30px;top:470px;width:220px;height:190px;border-radius:50%;
    background:radial-gradient(circle at 45% 40%,#f7e58e,var(--yuzu) 55%,#a88a2c 100%);
  }
  .art-figure{
    left:340px;top:330px;width:220px;height:450px;border-radius:45% 45% 10% 10%;
    background:linear-gradient(180deg,#3a2a22 0%,var(--skin-tone) 22%,var(--kimono) 50%,#6e1f1c 100%);
  }
  .origin-tag{
    position:absolute;left:170px;top:150px;padding:4px 10px;
    border:2px solid var(--gold);border-radius:8px;background:var(--navy);
    font-family:"Zen Antique",serif;font-size:34px;color:var(--gold-light);letter-spacing:4px;
  }
  .product-name{
    position:absolute;left:225px;top:215px;writing-mode:vertical-rl;
    font-family:"Zen Antique",serif;font-size:96px;line-height:1;color:var(--gold);
    letter-spacing:4px;
  }
  .tasting-note{
    position:absolute;left:140px;top:300px;writing-mode:vertical-rl;
    font-family:"Shippori Mincho B1",serif;font-size:18px;line-height:1.5;color:var(--gold-light);letter-spacing:3px;
  }
  .category{
    position:absolute;left:0;right:0;top:680px;text-align:center;
    font-family:"Great Vibes",cursive;font-size:40px;color:var(--gold-light);
  }
</style>
</head>
<body>
  <div class="neck-label">
    <div class="brand-small">雪見 桃ノ詩</div>
    <div class="fruit-mark" role="img" aria-label="柚子の実の小さな絵"></div>
  </div>

  <div class="oval-label">
    <div class="art art-foliage" role="img" aria-label="柚子の枝葉と実の装飾画"></div>
    <div class="art art-lamp" role="img" aria-label="レトロなガス灯の絵"></div>
    <div class="art art-yuzu" role="img" aria-label="柚子の実の絵"></div>
    <div class="art art-figure" role="img" aria-label="グラスを持つ着物姿の女性の絵"></div>
    <div class="origin-tag">雪見</div>
    <div class="product-name">桃ノ詩</div>
    <div class="tasting-note">ほのかな<br>ゆずの香り</div>
    <div class="category">Yuzu Liqueur</div>
  </div>
</body>
</html>
```